Eye-catching & Glamorous Labels for Skincare Bottles & Jars

We need new labels designed for our product range as we have been dormant for a few years and are now rebranding Velora Grace - Kindly Made Skincare. The label sizes are defined in the attached word document. All products have either a bright silver or a matte silver lid pump/spray so please keep this in mind.

We are open to colours and invite you to create bright trendy labels which are coordinated with the logo attached. The logo is not of any specific colour so dark on light, light on dark, tone on tone - we like purple / duck egg blue / turquoise WITH matte silver, however stronger colours like navy plus maroon with matte silver is also a strong favourite. If you feel inspired by a colour you think would be appropriate to Velora Grace please feel free to have a go.

A front section for product information is required and the back should include relevant details ie ingredients, company info, and a note that there has been no testing on animals.

The serum bottle will require a front and back label on a clear label in a pale colour to coordinate with the rest of the range. Size for this label is 35mm top edge, 25mm bottom edge, height 45mm - I have attached a picture of the serum bottle as they were originally pad printed. Please don't hesitate to contact me for any further information. Good luck!

Target Market(s)

Educated professional women 30-45 who are regular skincare users and looking for beautiful skincare products without animal derived ingredients and animal testing

Industry/Entity Type

Skin Care Product

Font styles to use
Serif
Sans Serif
Decorative
Script

Colors

Designer to choose colors to be used in the design.

Requirements
Must have
• Velora Grace Logo - eye catching design - not too busy or cramped.
Nice to have
• Is it possible to create a background pattern using a very small image of the logo? Just a thought.

```html
<!DOCTYPE html>
<html lang="en">
<head>
<meta charset="utf-8">
<title>Velora Grace Day Cream Labels</title>
<link rel="stylesheet" href="https://fonts.googleapis.com/css2?family=Raleway:wght@400;500;600;700&display=swap">
<style>
  :root {
    --teal: #2b7f8b;
    --teal-soft: #3c8e99;
    --label-base: #f8fcfd;
    --pattern-tint: #e3f2f5;
    --page: #ffffff;
    --badge: #dfe6e8;
  }
  * { margin: 0; padding: 0; box-sizing: border-box; }
  html, body { width: 1200px; height: 1200px; overflow: hidden; background: var(--page); }
  body { position: relative; font-family: "Raleway", sans-serif; color: var(--teal); }

  .label {
    position: absolute; top: 258px; width: 327px; height: 692px;
    background: var(--label-base);
    box-shadow: 0 0 8px rgba(0,0,0,0.22);
    overflow: hidden;
  }
  .label--front { left: 210px; }
  .label--back { left: 663px; width: 324px; }
  .label__pattern { position: absolute; inset: 0; width: 100%; height: 100%; }

  /* Front */
  .brand { position: absolute; top: 0; left: 0; right: 0; text-align: center; }
  .brand__dot {
    display: block; width: 54px; height: 54px; margin: 34px auto 0;
    border-radius: 50%; background: var(--teal);
  }
  .brand__name {
    margin-top: 30px; font-size: 22px; font-weight: 500; letter-spacing: 0.3px;
    text-transform: uppercase; padding-left: 105px;
  }
  .brand__tagline {
    font-size: 12px; font-weight: 500; text-transform: uppercase;
    padding-left: 105px; margin-top: 1px;
  }
  .product { position: absolute; left: 24px; top: 476px; }
  .product__name { font-size: 33px; font-weight: 400; color: var(--teal-soft); }
  .product__desc { margin-top: 8px; font-size: 17px; line-height: 22px; }
  .volume {
    position: absolute; left: 0; right: 0; top: 652px; text-align: center;
    font-size: 20px; font-weight: 600;
  }

  /* Back */
  .copy { position: absolute; inset: 0; font-size: 16px; line-height: 22px; }
  .copy__line { position: absolute; white-space: nowrap; }
  .copy__heading { font-weight: 600; }

  .origin {
    position: absolute; left: 18px; top: 627px; width: 249px; height: 45px;
    background: var(--page); display: flex; align-items: center; gap: 8px; padding-left: 4px;
  }
  .origin__badge { width: 38px; height: 38px; border-radius: 50%; background: var(--badge); flex: none; }
  .origin__text { font-size: 19px; line-height: 20px; }
  .origin__text strong { font-weight: 700; }
</style>
</head>
<body>

  <section class="label label--front" aria-label="Front label">
    <svg class="label__pattern" viewBox="0 0 327 692" preserveAspectRatio="none" role="img" aria-label="Faint repeating brand pattern on a pale turquoise diagonal panel">
      <polygon points="0,0 327,0 327,692" fill="var(--pattern-tint)"/>
    </svg>
    <header class="brand">
      <span class="brand__dot"></span>
      <p class="brand__name">Velora Grace</p>
      <p class="brand__tagline">Kindly Made Skincare</p>
    </header>
    <div class="product">
      <h1 class="product__name">Day Cream</h1>
      <p class="product__desc">Lorem ipsum dolor sit<br>amet, consectetuer</p>
    </div>
    <p class="volume">160 mL</p>
  </section>

  <section class="label label--back" aria-label="Back label">
    <svg class="label__pattern" viewBox="0 0 324 692" preserveAspectRatio="none" role="img" aria-label="Faint repeating brand pattern on a pale turquoise diagonal panel">
      <polygon points="0,0 10,0 324,690 324,692 0,692" fill="var(--pattern-tint)"/>
    </svg>
    <div class="copy">
      <span class="copy__line" style="left:36px;top:12px"><span class="copy__heading">INGREDIENTS:</span> ipsum dolor sit</span>
      <span class="copy__line" style="left:45px;top:34px">amet, consectetuer adipiscing</span>
      <span class="copy__line" style="left:54px;top:57px">elit, sed diam nonummy nibh</span>
      <span class="copy__line" style="left:64px;top:79px">euismod tincidunt ut laoreet</span>
      <span class="copy__line" style="left:74px;top:102px">dolore magna aliquam erat</span>
      <span class="copy__line" style="left:84px;top:123px">volutpat.</span>
      <span class="copy__line" style="left:106px;top:166px"><span class="copy__heading">HOW TO USE:</span> Ut wisi</span>
      <span class="copy__line" style="left:117px;top:189px">enim ad minim</span>
      <span class="copy__line" style="left:126px;top:210px">veniam, quis nostrud</span>
      <span class="copy__line" style="left:136px;top:232px">exerci tation ut</span>
      <span class="copy__line" style="left:147px;top:253px">aliquip ex ea</span>
      <span class="copy__line" style="left:156px;top:276px">commodo</span>
      <span class="copy__line" style="left:166px;top:297px">consequat.</span>
      <span class="copy__line" style="left:158px;top:318px">olestie</span>
      <span class="copy__line" style="left:187px;top:340px">consequat,</span>
      <span class="copy__line" style="left:198px;top:361px">vel illum</span>
      <span class="copy__line" style="left:208px;top:384px">dolore eu</span>
      <span class="copy__line" style="left:217px;top:405px">feugi</span>
    </div>
    <div class="origin">
      <span class="origin__badge" role="img" aria-label="No animal testing certification badge"></span>
      <p class="origin__text"><strong>Made in Australia</strong><br>by Velora Grace</p>
    </div>
  </section>

</body>
</html>
```